Corporate Brochure Cover Design

We need a design for a corporate A4 Size portfolio cover (front and back) which we will be distributing. to our commercial clients.

We are a professional plumbing company that is an industry leader for service we provide to our clients and technology we use. The design needs to incorporate the colours black, red, white and silver and needs to include our logo. We dont have any slogans or mottos... If you wanted to use something it could be "Delivering exceptional service...Always!" however i dont want it to b the focal point of the cover.

Im looking for something professional and modern that has the WOW factor!

Size is A4 - both front and back covers. You can include pictures as well or sample pictures of where we can source and put our own team pictures.

if you have any questions, please do not hesitate to contact me.

Target Market(s)

Our commercial & strata clients - professional industry.

Industry/Entity Type

Commercial

Font styles to use
Sans Serif

Requirements
Must have
• Red, black, white, silver as the colour scheme.
• Include the logo.
Nice to have
• Modern design and something that makes the client go WOW before they open the brochure.
Should not have
• lots of text

```html
<!DOCTYPE html>
<html lang="en">
<head>
<meta charset="utf-8">
<title>Meridian Portfolio Cover</title>
<link href="https://fonts.googleapis.com/css2?family=Roboto:wght@400;700&display=swap" rel="stylesheet">
<style>
  :root {
    --sheet: #ffffff;
    --cover: #111111;
    --red: #c8102e;
    --white: #ffffff;
    --silver: #b5b5b5;
    --label: #222222;
  }
  html, body {
    margin: 0;
    padding: 0;
    width: 1200px;
    height: 874px;
    overflow: hidden;
    background: var(--sheet);
    font-family: "Roboto", Arial, sans-serif;
  }
  .spread {
    position: relative;
    width: 1200px;
    height: 874px;
  }
  .cover {
    position: absolute;
    top: 24px;
    width: 548px;
    height: 749px;
    background: var(--cover);
    overflow: hidden;
  }
  .cover--back { left: 37px; }
  .cover--front { left: 599px; }
  .cover-label {
    position: absolute;
    top: 800px;
    width: 548px;
    text-align: center;
    font-size: 13px;
    color: var(--label);
  }
  .cover-label--back { left: 37px; }
  .cover-label--front { left: 599px; }

  .brand {
    position: absolute;
    display: flex;
    align-items: center;
    justify-content: center;
    gap: 8px;
    color: var(--white);
    font-weight: 700;
    letter-spacing: 1px;
  }
  .brand-dot {
    border-radius: 50%;
    background: var(--red);
  }
  .brand--front {
    left: 0;
    top: 62px;
    width: 548px;
    font-size: 36px;
  }
  .brand--front .brand-dot { width: 18px; height: 18px; }
  .brand--back {
    left: 74px;
    top: 525px;
    width: 400px;
    font-size: 20px;
  }
  .brand--back .brand-dot { width: 10px; height: 10px; }

  .stroke-art {
    position: absolute;
    left: 0;
    top: 373px;
    width: 548px;
    height: 260px;
    background: linear-gradient(100deg, var(--red) 0%, var(--red) 62%, var(--silver) 82%, var(--white) 100%);
  }

  .contact {
    position: absolute;
    left: 74px;
    top: 590px;
    width: 400px;
    text-align: center;
    color: var(--silver);
  }
  .contact-heading {
    margin: 0;
    font-size: 12.5px;
    font-weight: 400;
    letter-spacing: 1.6px;
  }
  .contact-address {
    margin: 14px 0 0;
    font-size: 9.5px;
    line-height: 14px;
    font-style: normal;
  }
  .contact-support {
    margin: 9px 0 0;
    font-size: 12px;
    letter-spacing: 1px;
    color: var(--red);
  }
  .contact-phone {
    margin: 2px 0 0;
    font-size: 12px;
    color: var(--white);
  }
  .contact-web {
    margin: 14px -20px 0;
    font-size: 9.5px;
    white-space: nowrap;
  }
</style>
</head>
<body>
<main class="spread">
  <section class="cover cover--back" aria-label="Back cover">
    <div class="brand brand--back">
      <span class="brand-dot"></span>
      <span class="brand-name">MERIDIAN</span>
    </div>
    <div class="contact">
      <h2 class="contact-heading">CORPORATE OFFICE</h2>
      <address class="contact-address">#48, HARBOUR VIEW LANE, EASTGATE.<br>NEW SOUTH BAY. AUSTRALIA. 204518</address>
      <p class="contact-support">SUPPORT</p>
      <p class="contact-phone">1800 274 5310, 1800 639 2148</p>
      <p class="contact-web">Email: hello@meridianplumbing.example &nbsp;|&nbsp; Web: www.meridianplumbing.example</p>
    </div>
  </section>

  <section class="cover cover--front" aria-label="Front cover">
    <div class="brand brand--front">
      <span class="brand-dot"></span>
      <span class="brand-name">MERIDIAN</span>
    </div>
    <div class="stroke-art" role="img" aria-label="Sweeping red and white brush-stroke artwork across the lower cover"></div>
  </section>

  <div class="cover-label cover-label--back">Back</div>
  <div class="cover-label cover-label--front">Front</div>
</main>
</body>
</html>
```